Label for Wines Design

I need a label design for a start-up business that makes grape wines. The label of wine features a picture frame on the edges of the wine bottle label. So each style of wine (red, white, sparkling, rose etc) will feature a different colour. As you can picture there is already a lot going on in this label.

My trademark is 'tamo', means 'Virgin pure love',type of wines: Sauvignon Blanc, Merlot, Pino noir etc. All in Caps, a Juxtaposition of old & modern. Bold & thick letters to grab attention on the wine store shelves. Maybe letter spacing squeezed together as the wine label is only 4inches wide...the text 'tamo' must fit on one line! No Cursive or curvy lines! Colors open to black, green, yellow, purple must be natural colors hues in nature.

New Zealand wines are New worlds wines,green and astringency,unique fruity, just as virgin pure love, is an infatuation, lovesickness, never forget......

Target Market(s)

New Zealand and Asian
food & wine lovers all ages

Industry/Entity Type

Business

Font styles to use
Decorative
Script

Colors

Designer to choose colors to be used in the design.

Requirements
Must have
• Front Label and back label
Nice to have
• Wines-feeling is green and astringency,unique fruity, just as virgin pure love, is an infatuation, lovesickness, never forget......

```html
<!DOCTYPE html>
<html lang="en">
<head>
<meta charset="utf-8">
<title>Tamo Wine Labels</title>
<link rel="stylesheet" href="https://fonts.googleapis.com/css2?family=Oswald:wght@300;400&display=swap">
<style>
  :root {
    --backdrop: #ededed;
    --white-frame: #9aab68;
    --white-panel: #eaecdc;
    --white-ink: #1d1d1b;
    --white-accent: #6f7f3e;
    --fern-white-light: #c9d99a;
    --fern-white-dark: #8fa159;
    --red-frame: #c4232b;
    --red-panel: #141113;
    --red-ink: #f2f0ee;
    --fern-red-light: #e8333a;
    --fern-red-dark: #7e1418;
  }
  * { box-sizing: border-box; margin: 0; padding: 0; }
  html, body {
    width: 1200px;
    height: 1000px;
    overflow: hidden;
    background: var(--backdrop);
  }
  .label-sheet {
    position: relative;
    width: 1200px;
    height: 1000px;
  }
  .label {
    position: absolute;
    top: 120px;
    width: 320px;
    height: 760px;
    padding: 12px;
    font-family: "Oswald", sans-serif;
  }
  .label--white { left: 230px; background: var(--white-frame); }
  .label--red { left: 650px; background: var(--red-frame); }
  .label__panel {
    position: relative;
    width: 100%;
    height: 100%;
  }
  .label--white .label__panel { background: var(--white-panel); color: var(--white-ink); }
  .label--red .label__panel { background: var(--red-panel); color: var(--red-ink); }
  .label__brand {
    position: absolute;
    top: 70px;
    left: 0;
    right: 0;
    text-align: center;
    font-weight: 400;
    font-size: 120px;
    line-height: 1;
    letter-spacing: -2px;
  }
  .label__fern {
    position: absolute;
    top: 250px;
    left: 18px;
    width: 240px;
    height: 340px;
    border-radius: 0 60% 0 60%;
  }
  .label--white .label__fern {
    background: linear-gradient(150deg, var(--fern-white-light), var(--fern-white-dark));
  }
  .label--red .label__fern {
    background: linear-gradient(150deg, var(--fern-red-light), var(--fern-red-dark));
  }
  .label__variety {
    position: absolute;
    top: 600px;
    left: 0;
    right: 0;
    text-align: center;
    font-weight: 300;
    font-size: 30px;
    letter-spacing: 0.5px;
  }
  .label__origin {
    position: absolute;
    top: 650px;
    left: 0;
    right: 0;
    text-align: center;
    font-weight: 300;
    font-size: 22px;
  }
  .label--white .label__variety,
  .label--white .label__origin { color: var(--white-accent); }
  .label__meta {
    position: absolute;
    top: 692px;
    left: 26px;
    right: 40px;
    display: flex;
    justify-content: space-between;
    align-items: baseline;
    font-weight: 300;
  }
  .label__abv { font-size: 13px; }
  .label__volume { font-size: 22px; }
</style>
</head>
<body>
  <main class="label-sheet">
    <section class="label label--white">
      <div class="label__panel">
        <h1 class="label__brand">TAMO</h1>
        <div class="label__fern" role="img" aria-label="Pale green fern frond illustration"></div>
        <p class="label__variety">SAUVIGNON BLANC</p>
        <p class="label__origin">WINE OF NEW ZEALAND</p>
        <div class="label__meta">
          <span class="label__abv">12% vol</span>
          <span class="label__volume">750ml</span>
        </div>
      </div>
    </section>
    <section class="label label--red">
      <div class="label__panel">
        <h1 class="label__brand">TAMO</h1>
        <div class="label__fern" role="img" aria-label="Red fern frond illustration"></div>
        <p class="label__variety">MERLOT</p>
        <p class="label__origin">WINE OF NEW ZEALAND</p>
        <div class="label__meta">
          <span class="label__abv">12% vol</span>
          <span class="label__volume">750ml</span>
        </div>
      </div>
    </section>
  </main>
</body>
</html>
```